Maple Hollow Bloom Panels Business card

Looking to have a business card design incorporating my logo for my flower wall business.

Industry/Entity Type

Wedding & event planning

Contact Information for Business Card

My business logo, my name - Lena Whitcombe (owner), my tagline - Let us be your something extra, phone # 401-726-3148, email address - maplehollowbloompanels@mailvane.net, my website - maplehollowbloompanels.net, Instagram handle- @maplehollowbloompanels, FB handle Handle - maplehollowbloompanels

Font styles to use
Other font styles liked:
• Sentaina is the font that is used in my logo

Requirements
Must have
• Would like a double sided business card

```html
<!DOCTYPE html>
<html lang="en">
<head>
<meta charset="utf-8">
<title>Maple Hollow Bloom Panels – Business Card</title>
<link href="https://fonts.googleapis.com/css2?family=Raleway:wght@400;500&display=swap" rel="stylesheet">
<style>
  :root {
    --backdrop: #000000;
    --gold-deep: #b47d16;
    --gold-mid: #d4a235;
    --gold-light: #f9e081;
    --ink: #2a241b;
    --icon-bg: #2b2722;
    --icon-fg: #ffffff;
    --badge: #ffffff;
    --veil: rgba(255, 246, 210, 0.22);
  }
  * { margin: 0; padding: 0; box-sizing: border-box; }
  html, body { width: 1200px; height: 1000px; overflow: hidden; background: var(--backdrop); }
  body { position: relative; font-family: "Raleway", sans-serif; color: var(--ink); }

  .card {
    position: absolute;
    left: 296px;
    width: 608px;
    height: 344px;
    border-radius: 18px;
    overflow: hidden;
    background: linear-gradient(30deg, var(--gold-deep) 0%, var(--gold-mid) 45%, var(--gold-light) 100%);
  }
  .card-front { top: 91px; }
  .card-back { top: 565px; }

  .bloom-motif {
    position: absolute;
    left: 250px; top: 12px;
    width: 318px; height: 316px;
    border-radius: 48% 52% 40% 60%;
    background: radial-gradient(ellipse at 55% 40%, var(--veil) 0%, rgba(255, 246, 210, 0.08) 70%, transparent 100%);
  }

  .owner-name {
    position: absolute;
    left: 16px; top: 8px;
    font-size: 32px; font-weight: 500;
    letter-spacing: 0.3px;
    white-space: nowrap;
  }
  .owner-title {
    position: absolute;
    left: 16px; top: 48px;
    width: 274px;
    text-align: center;
    font-size: 20px; font-weight: 500;
    letter-spacing: 5px;
  }

  .brand-badge {
    position: absolute;
    left: 25px; top: 110px;
    width: 168px; height: 168px;
    border-radius: 50%;
    background: var(--badge);
    display: flex; align-items: center; justify-content: center;
    text-align: center;
    padding: 22px;
    font-size: 17px; font-weight: 500;
    line-height: 1.3;
    color: var(--ink);
  }

  .contact-list { position: absolute; left: 222px; top: 78px; list-style: none; }
  .contact-item {
    display: flex; align-items: center;
    height: 36px; margin-bottom: 12.5px;
    font-size: 12.5px; font-weight: 500;
    letter-spacing: 0.2px;
    white-space: nowrap;
  }
  .contact-icon {
    width: 36px; height: 36px; border-radius: 50%;
    background: var(--icon-bg);
    margin-right: 12px;
    display: flex; align-items: center; justify-content: center;
    flex-shrink: 0;
  }
  .contact-icon svg { width: 20px; height: 20px; }

  .back-ring {
    position: absolute;
    left: 156px; top: 24px;
    width: 296px; height: 296px;
    border-radius: 50%;
    background: var(--veil);
  }
  .back-name {
    position: absolute;
    left: 0; right: 0; top: 148px;
    text-align: center;
    font-size: 40px; font-weight: 500;
    letter-spacing: 0.5px;
    white-space: nowrap;
  }
</style>
</head>
<body>

<section class="card card-front" aria-label="Business card front">
  <div class="bloom-motif" role="img" aria-label="Faint line drawing of a large peony bloom"></div>

  <h1 class="owner-name">LENA WHITCOMBE</h1>
  <p class="owner-title">OWNER</p>

  <div class="brand-badge">Maple Hollow Bloom Panels</div>

  <ul class="contact-list">
    <li class="contact-item">
      <span class="contact-icon">
        <svg viewBox="0 0 24 24" fill="none" stroke="var(--icon-fg)" stroke-width="1.7" stroke-linejoin="round"><path d="M5 3h4l2 5-2.5 1.5a11 11 0 0 0 6 6L16 13l5 2v4a2 2 0 0 1-2 2A16 16 0 0 1 3 5a2 2 0 0 1 2-2z"/></svg>
      </span>
      401-726-3148
    </li>
    <li class="contact-item">
      <span class="contact-icon">
        <svg viewBox="0 0 24 24" fill="none" stroke="var(--icon-fg)" stroke-width="1.7" stroke-linejoin="round"><rect x="3" y="5" width="18" height="14" rx="1"/><path d="M3 6l9 7 9-7"/></svg>
      </span>
      MAPLEHOLLOWBLOOMPANELS@MAILVANE.NET
    </li>
    <li class="contact-item">
      <span class="contact-icon">
        <svg viewBox="0 0 24 24" fill="none" stroke="var(--icon-fg)" stroke-width="1.6"><circle cx="12" cy="12" r="9"/><ellipse cx="12" cy="12" rx="4" ry="9"/><path d="M3 12h18M4.5 7.5h15M4.5 16.5h15"/></svg>
      </span>
      MAPLEHOLLOWBLOOMPANELS.NET
    </li>
    <li class="contact-item">
      <span class="contact-icon">
        <svg viewBox="0 0 24 24" fill="none" stroke="var(--icon-fg)" stroke-width="1.8" stroke-linecap="round"><circle cx="12" cy="12" r="3.5"/><path d="M15.5 8.5v5a2.5 2.5 0 0 0 5 0V12a8.5 8.5 0 1 0-3.5 6.9"/></svg>
      </span>
      @MAPLEHOLLOWBLOOMPANELS
    </li>
    <li class="contact-item">
      <span class="contact-icon">
        <svg viewBox="0 0 24 24" fill="none" stroke="var(--icon-fg)" stroke-width="1.7" stroke-linecap="round"><circle cx="12" cy="8" r="3.5"/><path d="M5 20a7 7 0 0 1 14 0"/></svg>
      </span>
      HANDLE HANDLE - MAPLEHOLLOWBLOOMPANELS
    </li>
  </ul>
</section>

<section class="card card-back" aria-label="Business card back">
  <div class="back-ring"></div>
  <p class="back-name">Maple Hollow Bloom Panels</p>
</section>

</body>
</html>
```